Brennoria Business Card Design

Primarily a Real Estate Investment company but also invests in other business ventures.
Updates

The attachments have been uploaded to give you a better perspective on what I'm looking for. Please pay close attention to the Tidal Gala Works card as a sample.Thank you.

Target Market(s)

Upper escalante individuals that would like to purchase real estate

Industry/Entity Type

Business

Contact Information for Business Card

Brennoria Holdings LLC, Sorelle A. Vantwick, CEO/MBA, 415-286-7304, Sorelle4816@mailbrook.net

Colors
0455a3
ffffff

Requirements
Must have
• Majority of card color MUST be Black ----- Like pictures 2&3
(pic4) Raised silver foil "B" to start the Brennoria name on the card.
(pic3) Love the whole layout, round edges, placement of contact info. {It is clean and elegant}
(pic1) Matte & Gloss backing
(pic2) Blue color (maybe the remainder of company name to make the card have pop of color).
Nice to have
• Silver foil siding

```html
<!DOCTYPE html>
<html lang="en">
<head>
<meta charset="utf-8">
<title>Brennoria Holdings LLC — Business Card</title>
<link rel="stylesheet" href="https://fonts.googleapis.com/css2?family=Cinzel:wght@400;600&family=Open+Sans:wght@400&display=swap">
<style>
  :root {
    --stage: #2b2b2b;
    --card: #1d1d1e;
    --card-back: #202021;
    --brand-blue: #0455a3;
    --silver: #9a9a9a;
    --white: #ffffff;
    --muted: #cfcfcf;
    --ghost: #3c3c3e;
  }
  * { box-sizing: border-box; margin: 0; padding: 0; }
  html, body {
    width: 1200px;
    height: 849px;
    overflow: hidden;
    background: var(--stage);
  }
  .canvas {
    position: relative;
    width: 1200px;
    height: 849px;
    display: flex;
    align-items: center;
    justify-content: center;
    gap: 60px;
  }
  .card {
    position: relative;
    width: 500px;
    height: 286px;
    border-radius: 14px;
    overflow: hidden;
    box-shadow: 0 10px 30px rgba(0,0,0,0.45);
  }

  /* Back side */
  .card--back {
    background: var(--card-back);
    display: flex;
    flex-direction: column;
    align-items: center;
    justify-content: center;
    gap: 22px;
  }
  .back-mark {
    width: 74px;
    height: 74px;
    border-radius: 50%;
    background: var(--ghost);
  }
  .back-name {
    font-family: "Cinzel", serif;
    font-weight: 600;
    font-size: 27px;
    letter-spacing: 1px;
    color: var(--ghost);
  }

  /* Front side */
  .card--front {
    background: var(--card);
  }
  .edge {
    position: absolute;
    top: 0;
    bottom: 0;
    width: 7px;
    background: linear-gradient(90deg, var(--brand-blue) 0 55%, var(--silver) 55% 100%);
  }
  .edge--left { left: 0; }
  .edge--right { right: 0; background: linear-gradient(90deg, var(--silver) 0 45%, var(--brand-blue) 45% 100%); }

  .company {
    position: absolute;
    left: 56px;
    top: 70px;
    display: flex;
    align-items: center;
    gap: 12px;
  }
  .company-dot {
    width: 16px;
    height: 16px;
    border-radius: 50%;
    background: var(--brand-blue);
  }
  .company-name {
    font-family: "Cinzel", serif;
    font-weight: 400;
    font-size: 25px;
    letter-spacing: 1px;
    color: var(--white);
  }

  .details {
    position: absolute;
    left: 56px;
    top: 150px;
    display: flex;
    align-items: stretch;
    gap: 14px;
  }
  .person {
    text-align: right;
    font-family: "Open Sans", sans-serif;
  }
  .person-name {
    font-size: 17px;
    color: var(--white);
    line-height: 1.3;
  }
  .person-title {
    font-size: 11px;
    color: var(--muted);
    letter-spacing: 0.5px;
  }
  .divider {
    width: 2px;
    background: var(--brand-blue);
  }
  .contact {
    list-style: none;
    font-family: "Open Sans", sans-serif;
    font-size: 14px;
    color: var(--white);
    display: flex;
    flex-direction: column;
    justify-content: center;
    gap: 6px;
  }
  .contact-item {
    display: flex;
    align-items: center;
    gap: 7px;
  }
  .contact-icon {
    width: 14px;
    height: 14px;
    flex: none;
  }
</style>
</head>
<body>
<main class="canvas">

  <section class="card card--back" aria-label="Card back">
    <div class="back-mark"></div>
    <p class="back-name">Brennoria Holdings LLC</p>
  </section>

  <section class="card card--front" aria-label="Card front">
    <span class="edge edge--left"></span>
    <span class="edge edge--right"></span>

    <div class="company">
      <span class="company-dot"></span>
      <h1 class="company-name">Brennoria Holdings LLC</h1>
    </div>

    <div class="details">
      <div class="person">
        <p class="person-name">S. Vantwick</p>
        <p class="person-title">CEO/MBA</p>
      </div>
      <span class="divider"></span>
      <ul class="contact">
        <li class="contact-item">
          <svg class="contact-icon" viewBox="0 0 14 14" aria-hidden="true">
            <circle cx="7" cy="7" r="7" fill="#0455a3"/>
            <rect x="3.5" y="4.5" width="7" height="5" fill="none" stroke="#fff" stroke-width="1"/>
            <polyline points="3.5,4.5 7,7.3 10.5,4.5" fill="none" stroke="#fff" stroke-width="1"/>
          </svg>
          <span>Sorelle4816@mailbrook.net</span>
        </li>
        <li class="contact-item">
          <svg class="contact-icon" viewBox="0 0 14 14" aria-hidden="true">
            <circle cx="7" cy="7" r="7" fill="#0455a3"/>
            <path d="M4.6 3.6 L6 3.4 L6.7 5.3 L5.8 6 Q6.6 7.7 8 8.3 L8.7 7.4 L10.6 8.1 L10.4 9.5 Q9.8 10.4 8.6 10.2 Q4.2 9.2 3.8 5 Q3.7 4 4.6 3.6 Z" fill="#fff"/>
          </svg>
          <span>415-286-7304</span>
        </li>
      </ul>
    </div>
  </section>

</main>
</body>
</html>
```